Brightmoor Deed Partners Stationery
BDP Stationery
Brightmoor Deed Partners Stationery - Real Estate
Creative Brief
Professional
Leopoldo Varnhusk II
Manager
4817 North Kettleridge Road, Suite 320 Coconut Grove, Florida 33187
lv@brightmoordeedpartners.example
www.brightmoordeedpartners.example
$100 bonus to winning designer upon designer creating duplicate design and stationery for "Brightmoor Deed Alliance"

```html
<!DOCTYPE html>
<html lang="en">
<head>
<meta charset="utf-8">
<title>Brightmoor Deed Partners Stationery</title>
<link href="https://fonts.googleapis.com/css2?family=Roboto:wght@400;500;700&family=Roboto+Condensed:wght@700&display=swap" rel="stylesheet">
<style>
  :root {
    --backdrop: #8a8a8a;
    --green: #5ccb3c;
    --green-deep: #3fae28;
    --navy: #1c2233;
    --ink: #2a2f3a;
    --paper: #ffffff;
    --muted: #5b606b;
  }
  * { box-sizing: border-box; margin: 0; padding: 0; }
  html, body { width: 1200px; height: 908px; overflow: hidden; }
  body {
    background: var(--backdrop);
    font-family: "Roboto", Arial, sans-serif;
    position: relative;
  }
  .card {
    position: absolute;
    top: 304px;
    width: 520px;
    height: 300px;
    border-radius: 18px;
    overflow: hidden;
  }
  .card-front {
    left: 60px;
    background: linear-gradient(135deg, var(--green) 0%, var(--green-deep) 100%);
  }
  .front-name {
    position: absolute;
    left: 40px;
    bottom: 44px;
    color: var(--paper);
    font-family: "Roboto Condensed", Arial, sans-serif;
    font-weight: 700;
    text-transform: uppercase;
    line-height: 1.1;
  }
  .front-name .main { display: block; font-size: 30px; letter-spacing: 0.5px; }
  .front-name .sub { display: block; font-size: 13px; letter-spacing: 7px; margin-top: 6px; }

  .card-back {
    left: 620px;
    background: var(--paper);
  }
  .brand {
    position: absolute;
    left: 34px;
    top: 42px;
    display: flex;
    align-items: center;
    gap: 12px;
  }
  .brand-square {
    width: 40px; height: 40px;
    background: var(--navy);
  }
  .brand-name {
    font-family: "Roboto Condensed", Arial, sans-serif;
    font-weight: 700;
    color: var(--navy);
    text-transform: uppercase;
    font-size: 21px;
    line-height: 1.05;
  }
  .person {
    position: absolute;
    right: 30px;
    top: 46px;
    text-align: right;
  }
  .person-name { font-size: 15px; color: var(--ink); font-weight: 500; }
  .person-role { font-size: 11px; color: var(--green-deep); margin-top: 3px; }
  .contact {
    position: absolute;
    left: 34px;
    top: 118px;
    font-size: 10.5px;
    color: var(--ink);
    line-height: 1.45;
  }
  .contact .address { margin-bottom: 6px; }
  .contact-row { display: flex; align-items: center; gap: 6px; }
  .contact-icon {
    width: 10px; height: 10px; border-radius: 50%;
    background: var(--green-deep);
    flex: none;
  }
  .accent {
    position: absolute;
    left: 0; bottom: 0;
    width: 520px; height: 70px;
  }
  .site-band {
    position: absolute;
    left: 0; right: 0; bottom: 0;
    height: 26px;
    display: flex;
    align-items: center;
    justify-content: flex-end;
    padding-right: 26px;
    font-size: 10px;
    color: var(--paper);
    letter-spacing: 0.3px;
  }
</style>
</head>
<body>
  <section class="card card-front" aria-label="Business card front">
    <div class="front-name">
      <span class="main">Brightmoor Deed</span>
      <span class="sub">Alliance</span>
    </div>
  </section>

  <section class="card card-back" aria-label="Business card back">
    <div class="brand">
      <span class="brand-square"></span>
      <span class="brand-name">Brightmoor Deed<br>Alliance</span>
    </div>
    <div class="person">
      <div class="person-name">Leopoldo Varnhusk II</div>
      <div class="person-role">Manager</div>
    </div>
    <div class="contact">
      <div class="address">4817 North Kettleridge Road, Suite 320<br>Coconut Grove, Florida 33187</div>
      <div class="contact-row"><span class="contact-icon"></span>305-555-0142</div>
      <div class="contact-row"><span class="contact-icon"></span>305-555-0178</div>
      <div class="contact-row"><span class="contact-icon"></span>305-555-0193</div>
      <div class="contact-row"><span class="contact-icon"></span>lv@brightmoordeedpartners.example</div>
    </div>
    <svg class="accent" viewBox="0 0 520 70" aria-hidden="true">
      <polygon points="0,26 150,26 186,44 520,44 520,70 0,70" fill="var(--green)"/>
      <polygon points="0,38 520,38 520,70 0,70" fill="var(--navy)" transform="translate(0,6)"/>
      <polygon points="0,44 170,44 200,60 520,60 520,70 0,70" fill="var(--navy)"/>
    </svg>
    <div class="site-band">www.brightmoordeedpartners.example</div>
  </section>
</body>
</html>
```